kleines Übersetzungsbüro sucht Design für Folder
Zielgruppe
Als Selbständige betreibe ich ein Italienisch-Übersetzungsbüro, das mit qualitativ hochwertigen Übersetzungen und maßgeschneidertem Service wirbt. Meine Tätigkeiten drehen sich um die Fachbereiche Recht und PR/Marketing/Corporate Communication.
Aufgabenstellung
Die Broschüre soll dynamisch,frisch, luftig, aber professionell wirken und gerne an den Stil meiner Website angelehnt sein.
Eine leicht minimalistische Gestaltung mit farbigen Akzenten (z.B. grafische Elemente) ist durchaus willkommen, aber nicht zwingend. Wenn das Endergebnis stimmig und überzeugend ist, lasse ich mich gerne umstimmen.
Auf das genaue Format des Folders möchte ich mich nicht festlegen. Ob einfach gefalzt, mit Wickel- oder Z-Falz: die Wahl überlasse ich Ihnen.
Der Folder soll zunächst nur per Mail übermittelt bzw. online verfügbar sein. Es empfiehlt sich also ein Format, bei dem die Inhalte überschaubar dargestellt sind und auf einen Blick erfasst werden können.
Alle CI-Farben sollten bei der Gestaltung berücksichtigt werden.
Vorgaben für die Verwendung vom Bildmaterial siehe hochgeladenes Briefingdokument.
Die Broschüre soll die Botschaft vermitteln, dass es sich lohnt auf einen dynamischen, zuverlässigen Profi zu setzen, der für einen immer da ist und pfiffige Leistungen erbringt.

```html
<!DOCTYPE html>
<html lang="de">
<head>
<meta charset="utf-8">
<title>Lingua Verde – Folder</title>
<link href="https://fonts.googleapis.com/css2?family=Fira+Sans+Condensed:wght@300;400&display=swap" rel="stylesheet">
<style>
:root{
  --bg:#000;
  --paper:#fff;
  --fold:#e2e2e2;
  --lime:#b8dc00;
  --green:#5fb31d;
  --head:#78bf1c;
  --text:#555;
  --cyan:#3fbcd6;
}
*{margin:0;padding:0;box-sizing:border-box}
html,body{width:1200px;height:848px;overflow:hidden;background:var(--bg)}
body{position:relative;font-family:"Fira Sans Condensed",sans-serif;color:var(--text)}
.spread{position:absolute;top:153px;width:570px;height:541px;background:var(--paper);overflow:hidden}
.spread--front{left:20px}
.spread--back{left:610px}
.panel{position:absolute;top:0;width:190px;height:541px}
.panel:nth-child(1){left:0}
.panel:nth-child(2){left:190px}
.panel:nth-child(3){left:380px}
.panel--shade-left{background:linear-gradient(90deg,var(--fold) 0,#fafafa 18px,#fff 40px)}
.panel--shade-right{background:linear-gradient(270deg,var(--fold) 0,#fafafa 14px,#fff 34px)}
.art{position:absolute;left:0;top:0;width:570px;height:541px}
.content{position:absolute;z-index:2}
h2{font-weight:300;color:var(--head);font-size:13px;line-height:1.15;margin-bottom:9px}
h2.large{font-size:16px}
p,li{font-size:5.6px;line-height:1.42;font-weight:400}
p{margin-bottom:6px}
ul{list-style:none;margin-bottom:6px}
.brand{position:absolute;z-index:2;left:0;width:190px;text-align:center}
.brand-mark{display:inline-block;width:12px;height:12px;border-radius:50%;background:var(--green);vertical-align:middle;margin-right:5px}
.brand-name{font-size:15px;font-weight:400;color:var(--cyan);vertical-align:middle}
.tagline{position:absolute;z-index:2;left:0;width:190px;text-align:center;color:var(--head);font-size:12px;font-weight:400;line-height:1.3}
.contact{position:absolute;z-index:2;left:0;width:190px;text-align:center}
.contact p{font-size:5.8px;line-height:1.5;margin:0}
</style>
</head>
<body>

<section class="spread spread--front" aria-label="Außenseite">
  <div class="panel panel--shade-right"></div>
  <div class="panel panel--shade-left"></div>
  <div class="panel panel--shade-left"></div>

  <svg class="art" viewBox="0 0 570 541">
    <defs>
      <clipPath id="coverClip"><rect x="0" y="0" width="190" height="541"/></clipPath>
      <linearGradient id="officeTone" x1="0" y1="0" x2="1" y2="1">
        <stop offset="0" stop-color="#dfe9f2"/>
        <stop offset="0.55" stop-color="#9fb6cc"/>
        <stop offset="1" stop-color="#e9eef3"/>
      </linearGradient>
    </defs>
    <g clip-path="url(#coverClip)">
      <path d="M0,0 H190 V6 Q80,4 0,10 Z" fill="var(--lime)"/>
      <ellipse cx="235" cy="168" rx="215" ry="160" fill="var(--lime)"/>
      <ellipse cx="242" cy="172" rx="204" ry="152" fill="var(--green)"/>
      <ellipse cx="250" cy="174" rx="195" ry="144" fill="url(#officeTone)" role="img" aria-label="Foto: Geschäftsleute beim Händeschütteln im Büro, im Vordergrund Diagramme auf dem Tisch"/>
    </g>
    <path d="M190,541 V520 Q360,560 570,470 V541 Z" fill="var(--lime)"/>
    <path d="M190,541 V532 Q380,556 570,495 V541 Z" fill="var(--green)"/>
  </svg>

  <div class="brand" style="top:345px"><span class="brand-mark"></span><span class="brand-name">Lingua Verde</span></div>
  <div class="tagline" style="top:380px">Italienisch-Übersetzungen<br>mit Pfiff – direkt vom Profi</div>
  <div class="contact" style="top:440px">
    <p>Lingua Verde</p>
    <p>Inh.: Chiara Ventoli</p>
    <p>Lindenweg 7</p>
    <p>66111 Musterstadt</p>
    <p>Tel.: 0681 5550123</p>
    <p>Mobil: 0152 5550198</p>
    <p>Web: www.linguaverde-office.de</p>
    <p>Mail: info@linguaverde-office.de</p>
  </div>

  <div class="content" style="left:220px;top:24px;width:150px">
    <h2>Einige Highlights aus meinem Portfolio</h2>
    <p>Speziell für juristische Texte wie: Verträge, AGB, Klagen, Urteile, Urkunden, gerichtliche Beschlüsse, Protokolle, Handelsregisterauszüge, Ausschreibungsunterlagen, Satzungen, Schriftsätze, usw.</p>
    <ul>
      <li>- Übersetzungen</li>
      <li>- Beglaubigungen</li>
      <li>- Einholung von Apostillen</li>
      <li>- 4- und 6-Augenkontrolle</li>
      <li>- Express-Service</li>
    </ul>
    <p>Speziell für PR- und Marketing- und imagesensible Texte wie: Pressemitteilungen, Websites, Newsletters, Mitarbeiter- und Kundenmagazine, Unternehmensberichte, Themenzeitungen, alle Texte für Kampagnen, Markt- und Organisationskommunikation, Corporate Reputation und Social Networks, usw.</p>
    <ul>
      <li>- Übersetzung, Adaptation und Transkreation in Informations- oder Publikationsqualität</li>
      <li>- Briefing im Vorfeld der Projektumsetzung</li>
      <li>- Erstellung kundenspezifischer Translation Memories</li>
      <li>- 4- und 6-Augenkontrolle</li>
      <li>- Gut-zum-Druck</li>
    </ul>
  </div>
  <div class="content" style="left:220px;top:322px;width:150px">
    <h2>Ihr direkter Draht zum Übersetzungsprofi</h2>
    <p>Wenn Sie eine Übersetzungsagentur beauftragen, haben Sie zwar einen direkten Ansprechpartner. Dieser ist jedoch nicht für Ihre Übersetzung zuständig, sondern bearbeitet lediglich den Auftrag und gibt ihn an einen Übersetzer weiter. Wer diese Übersetzung letztendlich macht, erfahren Sie meistens nicht, auch nicht, wie qualifiziert Ihr Übersetzer tatsächlich ist. Bei mir hingegen wissen Sie, mit wem Sie es zu tun haben. Ich bin Ihre unmittelbare Ansprechpartnerin, kann gezielt auf Ihre individuellen Wünsche und Bedürfnisse eingehen und in jeder Phase des Auftrags mit Ihnen gemeinschaftlich am Gelingen Ihres Projektes arbeiten. Auf dem kleinen Dienstweg ist die Zusammenarbeit nicht nur persönlicher, sondern auch effizienter und passgenauer – genau das, was Sie benötigen!</p>
  </div>
  <div class="content" style="left:408px;top:24px;width:146px">
    <h2>Ihre Investition in Qualität</h2>
    <p>Aufgrund ihres hohen administrativen Aufwands verlangen Übersetzungsagenturen ein nicht unerhebliches Honorar, der Übersetzer, der letzten Endes mit dem Auftrag betraut wird, erhält aber meistens nur einen minimalen Teil davon. Das heißt, auch wenn Sie selbst einen angemessenen Preis für Ihre Übersetzung zahlen, erledigt am anderen Ende jemand diese zu einem Dumping-Preis. Hier ist jedoch echte Qualität nicht zu erwarten. Investieren Sie daher lieber direkt in das Endprodukt eines Profis – ohne, dass ein zwischengeschalteter Vermittler weitere Kosten verursacht. Bei mir fließt jeder Cent garantiert in Qualitätsarbeit!</p>
  </div>
  <div class="content" style="left:408px;top:212px;width:146px">
    <h2>Meine Werte –<br>Ihr Mehrwert</h2>
    <p>Meine Werte sind Ihr garantierter Mehrwert. Da Sie keine Umwege über ein Vermittlungsbüro gehen müssen, führt Ihr Auftrag Sie direkt zu mir. Ich stehe Ihnen als persönliche Ansprechpartnerin zur Verfügung – auch in Zeiten, in denen Übersetzungsbüros längst in den Feierabend oder ins Wochenende gegangen sind. Auf kurzem Kommunikationsweg erreichen Sie mich nahezu jederzeit per E-Mail oder telefonisch. Das ist Ihr Vorteil, gerade wenn es mal mit einer Übersetzung besonders eilig sein sollte. Bei aller Unkompliziertheit werden Professionalität, Diskretion und Termineinhaltung bei mir großgeschrieben. Dabei biete ich Ihnen maximale Transparenz: In der Projektabwicklung, der Preisgestaltung und schließlich der Honorarabrechnung behalten Sie jederzeit den Überblick.</p>
    <p>Setzen Sie daher auf:</p>
    <ul>
      <li>-Professionalität</li>
      <li>-Transparenz</li>
      <li>-kurze Wege</li>
      <li>-persönliche Beziehungen</li>
      <li>-kompromisslose Qualität</li>
    </ul>
  </div>
</section>

<section class="spread spread--back" aria-label="Innenseite">
  <div class="panel panel--shade-right"></div>
  <div class="panel panel--shade-left"></div>
  <div class="panel panel--shade-left"></div>

  <svg class="art" viewBox="0 0 570 541">
    <defs>
      <linearGradient id="deskTone" x1="0" y1="0" x2="0" y2="1">
        <stop offset="0" stop-color="#dcdcd8"/>
        <stop offset="0.7" stop-color="#f2f2f0"/>
        <stop offset="1" stop-color="#ffffff" stop-opacity="0"/>
      </linearGradient>
      <linearGradient id="portraitTone" x1="0" y1="0" x2="0" y2="1">
        <stop offset="0" stop-color="#f3f3f3"/>
        <stop offset="0.55" stop-color="#e4cfc2"/>
        <stop offset="1" stop-color="#2f9a45"/>
      </linearGradient>
      <clipPath id="portraitClip"><ellipse cx="300" cy="548" rx="88" ry="72"/></clipPath>
    </defs>
    <rect x="0" y="0" width="570" height="92" fill="url(#deskTone)" role="img" aria-label="Foto: Schreibtisch von oben mit Grünpflanzen, Notizblock, Stiften, Kaffeetasse und Tastatur"/>
    <path d="M0,480 Q120,545 300,541 L0,541 Z" fill="var(--lime)"/>
    <path d="M0,500 Q150,550 330,541 L0,541 Z" fill="var(--green)"/>
    <path d="M380,541 Q480,520 570,455 V541 Z" fill="var(--lime)"/>
    <path d="M390,541 Q490,530 570,480 V541 Z" fill="var(--green)"/>
    <ellipse cx="300" cy="548" rx="96" ry="80" fill="none" stroke="var(--lime)" stroke-width="10"/>
    <ellipse cx="300" cy="548" rx="90" ry="74" fill="none" stroke="var(--green)" stroke-width="3"/>
    <rect x="240" y="474" width="120" height="67" fill="url(#portraitTone)" clip-path="url(#portraitClip)" role="img" aria-label="Porträtfoto der Übersetzerin im grünen Oberteil"/>
  </svg>

  <div class="content" style="left:28px;top:118px;width:146px">
    <h2 class="large">Wenn Großes im Kleinen entsteht</h2>
    <p>Qualität war schon immer eine Frage des Könnens – das gilt insbesondere auch für den Übersetzungsbereich. Deshalb überzeugt mein Büro Lingua Verde seit über 13 Jahren private Kunden, Behörden und die unterschiedlichsten Akteure der freien Wirtschaft mit einem hochprofessionellen Übersetzungsservice, der keine Wünsche offen lässt. Frei nach dem Motto „Klein, aber fein“.</p>
    <p>Vielleicht kann ich bald auch Sie überzeugen. Unterhalten Sie Rechtsbeziehungen mit Kunden, Geschäftspartnern oder Zweigstellen Ihrer Organisation in Italien? Nehmen Sie dort an Ausschreibungen teil? Oder planen Sie etwa Marketing-Aktivitäten oder PR-Kampagnen für Ihre Zielgruppen im italienischen Sprachraum? Dann bin ich</p>
    <h2>Ihre Ansprechpartnerin und Wegbegleiterin für Italienisch-Fachübersetzungen.</h2>
  </div>
  <div class="content" style="left:222px;top:118px;width:146px">
    <ul>
      <li>Chiara Ventoli</li>
      <li>Dottoressa in Traduzione</li>
      <li>Italienisch Deutsch Englisch</li>
      <li>Allg. vereid. Übersetzerin und Dolmetscherin</li>
      <li>Mitglied im VFÜ e.V und BVSD e.V.</li>
      <li>Übersetzerin</li>
      <li>Korrektorin</li>
      <li>Transkreative Texterin</li>
    </ul>
    <p style="margin-top:6px">Als Italienisch-Muttersprachlerin verfüge ich über jene fundierte Sprachkenntnis und -sensibilität, die für Ihre Fachtexte unentbehrlich ist. Seit mehr als einem Jahrzehnt bin ich als selbständige Übersetzerin für hochwertige Fachtexte tätig. Meine akademische Ausbildung ergänze ich durch regelmäßige Weiterbildungsmaßnahmen, so dass ich in puncto Fachwissen, Know-How, Allgemeinbildung und Sprachpflege kontinuierlich an Erfahrung dazugewinne. Um eine qualitativ einwandfreie Leistung liefern zu können, setze ich die neuesten CAT-Technologien des Marktes ein, wie die Software LexiSuite 2015. Weil Technik und erworbene Kompetenz nicht alles sind, werfe ich außerdem meine Talente wie große Sprachgewandtheit, Kreativität und Feingefühl mit auf die Waage, damit Sie am Ende des Tages eine perfekte Übersetzung auf dem Schreibtisch haben.</p>
  </div>
  <div class="content" style="left:410px;top:118px;width:146px">
    <p>Juristische Übersetzungen und Übersetzungen im Bereich des Marketing und PR – auf diese beiden Schwerpunkte habe ich mich spezialisiert. Erstere bedürfen absoluter Präzision. Gerade juristische Texte müssen eindeutig und genau formuliert werden. Selbst kleinste Ungenauigkeiten und Fehler in der Übersetzung können großen Schaden nach sich ziehen. Hier sollten Sie nichts dem Zufall überlassen, da nicht nur Texte übersetzt werden, sondern auch die Besonderheiten zweier Rechtssysteme berücksichtigt werden müssen. Dank meiner einschlägigen Berufserfahrung verfüge ich über solide juristische Kenntnisse und garantiere Ihnen die strikte Einhaltung der Prinzipien der Rechtsübersetzung. Diskretion versteht sich von selbst. So sind Sie auf der sicheren Seite!</p>
    <p>Übersetzungen für Marketing und Public Relations sind hingegen deutlich vielschichtiger. Hier geht es nicht um wortgenaue Übersetzungen, sondern darum, eine Zielgruppe mit einem anderen sprachlichen und kulturellen Hintergrund zu erreichen und zu bewegen. Dazu brauchen Sie die griffigen, knackigen und zielsprachlich authentischen Übersetzungen eines Spezialisten für Adaptation und Transkreation. Mit meiner ausgeprägten interkulturellen Sensibilität, textlichen Kreativität und meinem unerschöpflichen Repertoire an Schreib- und Übersetzungstechniken gelingt mir der Spagat zwischen Sprachen und Kulturen. Gemeinsam steigern wir die rationale und emotionale Attraktivität Ihres Images bei Ihrer Zielgruppe in Italien und Tessin.</p>
  </div>
</section>

</body>
</html>
```